A online shop for solid wood need a Stationary design

A new online shop (in Austria and Germany) for solid wood and steel furniture (feldberg-formwerk) needs a Stationay design (letterhead, business card, envelope etc...). Dining tables, coffee tables, TV furniture and similar furniture will be sold. Everything will be custom made.

```html
<!DOCTYPE html>
<html lang="en">
<head>
<meta charset="utf-8">
<title>Feldberg Formwerk – Stationery</title>
<link href="https://fonts.googleapis.com/css2?family=Montserrat:wght@700&family=Roboto:wght@400;500&display=swap" rel="stylesheet">
<style>
  :root{
    --brand-red:#ec1c24;
    --paper:#ffffff;
    --ink:#3a3a3a;
    --muted:#6b6b6b;
    --band-grey:#b3b5b7;
    --backdrop:#b3b8b2;
  }
  *{box-sizing:border-box;margin:0;padding:0}
  html,body{width:1200px;height:675px;overflow:hidden}
  body{background:var(--backdrop);position:relative;font-family:'Roboto',Arial,sans-serif;color:var(--ink)}
  .sheet{position:absolute;background:var(--paper);box-shadow:0 2px 5px rgba(0,0,0,.18);overflow:hidden}
  .brand{font-family:'Montserrat',Arial,sans-serif;font-weight:700;letter-spacing:.08em;text-transform:uppercase;display:flex;align-items:center;white-space:nowrap}
  .brand .mark{display:inline-block;background:currentColor;margin-right:.45em}
  .footer-band{position:absolute;left:0;right:0;bottom:0;background:linear-gradient(115deg,var(--brand-red) 0 62%,#fff 62% 62.6%,var(--band-grey) 62.6%)}
  .contact-row{position:absolute;display:flex;align-items:center;color:var(--ink)}
  .contact-group{display:flex;flex-direction:column}
  .contact-line{display:flex;align-items:center;gap:.35em}
  .contact-line svg{flex:none}
  .contact-divider{background:var(--brand-red);align-self:stretch}

  /* folder cover */
  .folder{left:283px;top:67px;width:278px;height:369px;background:var(--brand-red);color:#fff}
  .folder .brand{position:absolute;left:0;right:0;top:170px;justify-content:center;font-size:17px}
  .folder .brand .mark{width:14px;height:14px}
  .folder-url{position:absolute;left:0;right:0;top:338px;text-align:center;font-size:7.6px}

  /* letterhead */
  .letterhead{left:585px;top:71px;width:255px;height:360px}
  .letterhead .brand{position:absolute;left:27px;top:52px;color:var(--brand-red);font-size:7px}
  .letterhead .brand .mark{width:7px;height:7px}
  .letter-body{position:absolute;left:27px;top:91px;width:201px;font-size:4.4px;line-height:6.65px;text-align:justify;color:var(--muted)}
  .letter-body p{margin-bottom:6.6px}
  .letterhead .contact-row{left:27px;top:335px;font-size:4.8px;line-height:6.5px;gap:8px}
  .letterhead .contact-divider{width:.6px}
  .letterhead .footer-band{height:5px}

  /* DL envelope, front */
  .envelope-front{left:236px;top:457px;width:267px;height:121px}
  .envelope-front .brand{position:absolute;left:17px;top:40px;color:var(--brand-red);font-size:7.4px}
  .envelope-front .brand .mark{width:7px;height:7px}
  .envelope-front .contact-row{left:17px;top:96px;font-size:4.9px;line-height:6.5px;gap:14px}
  .envelope-front .contact-divider{width:.7px}
  .envelope-front .footer-band{height:5px}

  /* DL envelope, back */
  .envelope-back{left:523px;top:457px;width:267px;height:122px}
  .envelope-flap{position:absolute;left:0;top:0;width:100%;height:41px;background:var(--brand-red);border-radius:0 0 20px 20px;display:flex;align-items:center;justify-content:center}
  .envelope-flap .brand{color:#fff;font-size:9px}
  .envelope-flap .brand .mark{width:8px;height:8px}

  /* business card, front */
  .card-front{left:811px;top:457px;width:109px;height:62px;background:var(--brand-red);color:#fff}
  .card-front .brand{position:absolute;left:0;right:0;top:22px;justify-content:center;font-size:6.2px}
  .card-front .brand .mark{width:5px;height:5px}
  .card-url{position:absolute;left:0;right:0;top:51px;text-align:center;font-size:2.8px}

  /* business card, back */
  .card-back{left:811px;top:540px;width:109px;height:62px}
  .card-back .brand{position:absolute;left:6px;top:27px;color:var(--brand-red);font-size:3.6px;letter-spacing:.04em}
  .card-back .brand .mark{width:3px;height:3px}
  .card-rule{position:absolute;left:53px;top:15px;width:.5px;height:34px;background:var(--brand-red)}
  .card-details{position:absolute;left:56px;top:15px;font-size:2.6px;line-height:3.6px;color:var(--ink)}
  .card-name{color:var(--brand-red);font-weight:500;font-size:3.4px;line-height:4px}
  .card-role{margin-bottom:2.6px}
  .card-back .footer-band{height:3.5px}
</style>
</head>
<body>

  <!-- Folder cover -->
  <section class="sheet folder" aria-label="Presentation folder">
    <div class="brand"><span class="mark"></span>Feldberg Formwerk</div>
    <p class="folder-url">www.feldbergformwerk.com</p>
  </section>

  <!-- Letterhead -->
  <section class="sheet letterhead" aria-label="Letterhead">
    <div class="brand"><span class="mark"></span>Feldberg Formwerk</div>
    <div class="letter-body">
      <p>Dear customer,</p>
      <p>Lorem ipsum dolor sit amet, consectetur adipisicing elit, sed do eiusmod tempor incididunt ut labore et dolore magna aliqua. Ut enim ad minim veniam, quis nostrud exercitation ullamco laboris nisi ut aliquip ex ea commodo consequat. Duis aute irure dolor in reprehenderit in voluptate velit esse cillum dolore eu fugiat nulla pariatur. Excepteur sint occaecat cupidatat non proident, sunt in culpa qui officia deserunt mollit anim id est laborum.</p>
      <p>Lorem ipsum dolor sit amet, consectetur adipisicing elit, sed do eiusmod tempor incididunt ut labore et dolore magna aliqua. Ut enim ad minim veniam, quis nostrud exercitation ullamco laboris nisi ut aliquip ex ea commodo consequat. Duis aute irure dolor in reprehenderit in voluptate velit esse cillum dolore eu fugiat nulla pariatur. Excepteur sint occaecat cupidatat non proident, sunt in culpa qui officia deserunt mollit anim id est laborum.</p>
      <p>Lorem ipsum dolor sit amet, consectetur adipisicing elit, sed do eiusmod tempor incididunt ut labore et dolore magna aliqua. Ut enim ad minim veniam, quis nostrud exercitation ullamco laboris nisi ut aliquip ex ea commodo consequat. Duis aute irure dolor in reprehenderit in voluptate velit esse cillum dolore eu fugiat nulla pariatur. Excepteur sint occaecat cupidatat non proident, sunt in culpa qui officia deserunt mollit anim id est laborum.</p>
      <p>Lorem ipsum dolor sit amet, consectetur adipisicing elit, sed do eiusmod tempor incididunt ut labore et dolore magna aliqua. Ut enim ad minim veniam, quis nostrud exercitation ullamco laboris nisi ut aliquip ex ea commodo consequat. Duis aute irure dolor in reprehenderit.</p>
      <p>Yours Sincerely,</p>
    </div>
    <div class="contact-row">
      <div class="contact-group">
        <span class="contact-line"><svg width="4" height="4" viewBox="0 0 10 10"><path d="M2 0l2 2.5-1.2 1.3a6 6 0 0 0 3.4 3.4L7.5 6 10 8l-1.5 2C4 10 0 6 0 1.5z" fill="#ec1c24"/></svg>+43 512 390 4471</span>
        <span class="contact-line"><svg width="4" height="4" viewBox="0 0 10 10"><rect x="2.5" y="0" width="5" height="3" fill="#ec1c24"/><rect x="0" y="3.5" width="10" height="4" fill="#ec1c24"/><rect x="2.5" y="8" width="5" height="2" fill="#ec1c24"/></svg>+43 512 390 4471</span>
      </div>
      <span class="contact-divider"></span>
      <div class="contact-group">
        <span class="contact-line"><svg width="4" height="4" viewBox="0 0 10 10"><rect x="0" y="1.5" width="10" height="7" fill="#ec1c24"/><path d="M0 1.5l5 4 5-4" stroke="#fff" fill="none"/></svg>hallo@feldbergformwerk.com</span>
        <span class="contact-line"><svg width="4" height="4" viewBox="0 0 10 10"><circle cx="5" cy="5" r="4.3" stroke="#ec1c24" fill="none" stroke-width="1.2"/><path d="M.7 5h8.6M5 .7c-2.5 2.5-2.5 6 0 8.6M5 .7c2.5 2.5 2.5 6 0 8.6" stroke="#ec1c24" fill="none"/></svg>www.feldbergformwerk.com</span>
      </div>
      <span class="contact-divider"></span>
      <div class="contact-group">
        <span>Lindenweg 14</span>
        <span>6020 Innsbruck, Austria</span>
      </div>
    </div>
    <div class="footer-band"></div>
  </section>

  <!-- Envelope front -->
  <section class="sheet envelope-front" aria-label="Envelope, front">
    <div class="brand"><span class="mark"></span>Feldberg Formwerk</div>
    <div class="contact-row">
      <div class="contact-group">
        <span class="contact-line"><svg width="4.5" height="4.5" viewBox="0 0 10 10"><path d="M2 0l2 2.5-1.2 1.3a6 6 0 0 0 3.4 3.4L7.5 6 10 8l-1.5 2C4 10 0 6 0 1.5z" fill="#ec1c24"/></svg>+43 512 390 4471</span>
        <span class="contact-line"><svg width="4.5" height="4.5" viewBox="0 0 10 10"><rect x="2.5" y="0" width="5" height="3" fill="#ec1c24"/><rect x="0" y="3.5" width="10" height="4" fill="#ec1c24"/><rect x="2.5" y="8" width="5" height="2" fill="#ec1c24"/></svg>+43 512 390 4471</span>
      </div>
      <span class="contact-divider"></span>
      <div class="contact-group">
        <span class="contact-line"><svg width="4.5" height="4.5" viewBox="0 0 10 10"><rect x="0" y="1.5" width="10" height="7" fill="#ec1c24"/><path d="M0 1.5l5 4 5-4" stroke="#fff" fill="none"/></svg>hallo@feldbergformwerk.com</span>
        <span class="contact-line"><svg width="4.5" height="4.5" viewBox="0 0 10 10"><circle cx="5" cy="5" r="4.3" stroke="#ec1c24" fill="none" stroke-width="1.2"/><path d="M.7 5h8.6M5 .7c-2.5 2.5-2.5 6 0 8.6M5 .7c2.5 2.5 2.5 6 0 8.6" stroke="#ec1c24" fill="none"/></svg>www.feldbergformwerk.com</span>
      </div>
      <span class="contact-divider"></span>
      <div class="contact-group">
        <span>Lindenweg 14</span>
        <span>6020 Innsbruck, Austria</span>
      </div>
    </div>
    <div class="footer-band"></div>
  </section>

  <!-- Envelope back -->
  <section class="sheet envelope-back" aria-label="Envelope, back">
    <div class="envelope-flap">
      <div class="brand"><span class="mark"></span>Feldberg Formwerk</div>
    </div>
  </section>

  <!-- Business card front -->
  <section class="sheet card-front" aria-label="Business card, front">
    <div class="brand"><span class="mark"></span>Feldberg Formwerk</div>
    <p class="card-url">www.feldbergformwerk.com</p>
  </section>

  <!-- Business card back -->
  <section class="sheet card-back" aria-label="Business card, back">
    <div class="brand"><span class="mark"></span>Feldberg Formwerk</div>
    <span class="card-rule"></span>
    <div class="card-details">
      <p class="card-name">LENA HOFBAUER</p>
      <p class="card-role">Managing Director</p>
      <p>Werkstatt 3, Lindenweg 14</p>
      <p>6020 Innsbruck</p>
      <p>Austria</p>
      <p>+43 512 390 4472</p>
      <p>hallo@feldbergformwerk.com</p>
      <p>www.feldbergformwerk.com</p>
    </div>
    <div class="footer-band"></div>
  </section>

</body>
</html>
```